Creation of a Facebook cover graphic

We need a Facebook cover graphic for a page that will be used to test the market for an online training product.

The Product

The subject of the training is the basic online marketing. The training will be delivered online rather than at a venue.

The name of the website is www.tallowfinchhub.com. PLEASE NOTE We have owned the site domain for a while and the current content is 'NOT' representative of the new product. If Quillbarrow deliver on this project we will be back for the website and logo designs! please note we have included a draft logo concept file attachment with the brief.

Design Details

The cover graphic will be viewed on desktop, tablet and mobile. We have tried to give you a brief that guarantees the profile looks good and is readable on mobile. The design is bold and simple in order to enhance viewing the graphic on mobile.

We have included a draft graphic (Both as psd and png). This only shows layout and content. The draft graphic is mainly text based.

We have also included a concept file for the logo. You may want to incorporate the target and arrow icon contained in that file into the design.

Creating a design optimised for mobile is perhaps more challenging than larger formats. Feel free to designs with the following elements: Backgrounds; shapes; gradients and font/text effects - however try and retain a flat and simple design

Graphic size: 828px x 315px – we prefer this size rather than the mobile specific size. It actually renders best across all devices.
Place the design in between 174px & 650px horizontally as this gives best viewing on mobile. Backgrounds can extend across the whole graphic.
Web resolution

There are 2 section to the design:

Section 1. Title ‘The Bright Harbour Crew’
Section 2. Sub title ’Solving online marketing needs’ and to do listing

For the logo colouring and background we would prefer:

Background colour: #236d99 will be our main corporate colour. Other colours are #00456e, #236d99 and # 82bcd0.
Text colour : white or white with a shade of blue. You may contrast text colour of section 1 and section 2.

Fonts : We have two font styles in the draft (Arial Black and Arial Nova). The mobile first design requires the fonts to be very simple so as the text can be read on mobile devices. You can try similar such as Helvetica, Lato etc.
Icons etc : There are 3 ticks against each element of the to do list. Feel free to creative how you want to work with these.

Examples

The Quillbarrow graphic included in the files is a good example of simplicity and flat design.

Target Market(s)

Our clients will be business owners and managers. Generally, one person, small and medium sized businesses.
Gender : Both male and female.
Typical ages : 35-65
They favour simplicity, functionality and boldness - rather than elegance or sophistication

Industry/Entity Type

Marketing

Font styles to use
Sans Serif

Requirements
Must have
• View well on mobile devices
• Text readable on mobile devices
• Simplicity
• Flatter type of design
Nice to have
• Not really a design idea. Would like some feedback on whether our design brief was useful for you as designers.
Should not have
• Complex and finely detailed design

```html
<!DOCTYPE html>
<html lang="en">
<head>
<meta charset="utf-8">
<title>The Bright Harbour Crew – Cover</title>
<link rel="stylesheet" href="https://fonts.googleapis.com/css2?family=Archivo+Black&family=Arimo:wght@400&display=swap">
<style>
  :root {
    --page-bg: #e9ebee;
    --cover-navy: #00456e;
    --accent-sky: #82bcd0;
    --text-white: #ffffff;
  }
  html, body {
    margin: 0;
    padding: 0;
    width: 1200px;
    height: 900px;
    overflow: hidden;
    background: var(--page-bg);
  }
  .cover {
    position: absolute;
    left: 50px;
    top: 241px;
    width: 1100px;
    height: 418px;
    background: var(--cover-navy);
    color: var(--text-white);
  }
  .cover-title {
    position: absolute;
    left: 118px;
    top: 80px;
    margin: 0;
    font-family: "Archivo Black", "Arial Black", sans-serif;
    font-weight: 400;
    font-size: 52px;
    line-height: 60px;
    letter-spacing: 0.3px;
  }
  .cover-title span { display: block; }
  .cover-tagline {
    position: absolute;
    left: 459px;
    top: 86px;
    margin: 0;
    font-family: "Arimo", Arial, sans-serif;
    font-weight: 400;
    font-size: 37px;
    line-height: 46px;
  }
  .needs-list {
    position: absolute;
    left: 466px;
    top: 168px;
    margin: 0;
    padding: 0;
    list-style: none;
    font-family: "Arimo", Arial, sans-serif;
    font-size: 35px;
    line-height: 44px;
  }
  .needs-list li {
    display: flex;
    align-items: center;
    height: 57px;
  }
  .needs-marker {
    width: 34px;
    height: 34px;
    margin-right: 49px;
    flex: none;
  }
</style>
</head>
<body>
  <section class="cover" aria-label="The Bright Harbour Crew cover graphic">
    <h1 class="cover-title">
      <span>The</span>
      <span>Bright</span>
      <span>Harbour</span>
      <span>Crew</span>
    </h1>
    <p class="cover-tagline">Solving online marketing needs</p>
    <ul class="needs-list">
      <li>
        <svg class="needs-marker" viewBox="0 0 34 34" aria-hidden="true"><circle cx="17" cy="17" r="15" fill="var(--accent-sky)"/></svg>
        Making web sites ‘sticky’
      </li>
      <li>
        <svg class="needs-marker" viewBox="0 0 34 34" aria-hidden="true"><circle cx="17" cy="17" r="15" fill="var(--accent-sky)"/></svg>
        Increasing conversions
      </li>
      <li>
        <svg class="needs-marker" viewBox="0 0 34 34" aria-hidden="true"><circle cx="17" cy="17" r="15" fill="var(--accent-sky)"/></svg>
        Boosting quality traffic
      </li>
    </ul>
  </section>
</body>
</html>
```